Wordpress website design for Pelix Bridge-Africa

We need a website for a new consultancy and digital marketplace in Kenya called 'Pelix Bridge - Africa'. Please refer to the the attached document [Pelix Bridge Africa website brief] and contact me anytime.

Bests,
Rosalind
Updates

Deadline extended to allow for additional revisions and refinements, ensuring that final designs align closely with project objectives and quality standards. This extra time will help incorporate valuable feedback and ensure the final output meets our high expectations.

Coding

```html
<!DOCTYPE html>
<html lang="en">
<head>
<meta charset="utf-8">
<title>Pelix Bridge Africa</title>
<link href="https://fonts.googleapis.com/css2?family=Poppins:wght@400;500;600;700&display=swap" rel="stylesheet">
<style>
:root{
  --navy:#1c3a5c;
  --navy-dark:#17304d;
  --green:#2eaa4a;
  --ink:#1c2b3d;
  --muted:#6b7683;
  --soft:#f2f3f4;
  --line:#e3e6ea;
  --white:#ffffff;
}
*{box-sizing:border-box;margin:0;padding:0}
html,body{width:1200px;height:2920px;overflow:hidden}
body{font-family:"Poppins",sans-serif;color:var(--ink);background:var(--white);position:relative}
.abs{position:absolute}
.brand{display:flex;align-items:center;gap:10px;font-weight:700;font-size:22px;color:var(--navy);letter-spacing:.5px;white-space:nowrap}
.brand-dot{width:30px;height:30px;border-radius:50%;background:var(--green)}
.btn{display:inline-block;background:var(--green);color:var(--white);font-size:12px;font-weight:500;padding:10px 22px;border-radius:3px;white-space:nowrap}
.btn-outline{display:inline-block;border:1px solid var(--line);color:var(--ink);font-size:12px;padding:8px 22px;border-radius:3px}

/* header + hero */
.hero{left:0;top:0;width:1200px;height:600px;background:linear-gradient(180deg,#f4f5f4,#ecedec)}
.hero-photo{left:600px;top:0;width:600px;height:600px;background:linear-gradient(135deg,#6b5a48,#3c3a38 55%,#8d7a62)}
.site-header{left:0;top:0;width:1200px;height:90px}
.site-header .brand{position:absolute;left:100px;top:30px}
.nav{position:absolute;left:400px;top:38px;display:flex;gap:20px;font-size:11px;color:var(--ink);white-space:nowrap}
.nav .active{border:1px solid var(--line);padding:3px 10px;margin-top:-4px;background:var(--white)}
.header-phone{position:absolute;left:900px;top:38px;font-size:11px;color:var(--white);white-space:nowrap}
.site-header .btn{position:absolute;left:1030px;top:28px}
.hero-title{left:100px;top:170px;font-size:48px;line-height:1.15;font-weight:600;color:var(--navy)}
.hero-sub{left:100px;top:360px;width:330px;font-size:13px;line-height:1.5;color:var(--ink)}
.hero-cta{left:100px;top:430px;display:flex;align-items:center;gap:12px;font-size:13px;color:var(--green)}
.hero-cta span{width:36px;height:36px;border-radius:50%;background:var(--green);display:flex;align-items:center;justify-content:center}

/* about */
.about-photo{left:200px;top:700px;width:340px;height:320px;background:linear-gradient(135deg,#dfe3e2,#9a8a78 60%,#c8c0b2)}
.about-frame{left:230px;top:690px;width:320px;height:300px;border:2px solid var(--line);background:transparent}
.about-text{left:610px;top:690px;width:420px}
.eyebrow{font-size:11px;color:var(--green);margin-bottom:10px}
.about-text h2{font-size:24px;line-height:1.35;font-weight:600;color:var(--navy);margin-bottom:16px}
.about-text p{font-size:11px;line-height:1.6;color:var(--muted);margin-bottom:22px}

/* services */
.services-head{left:100px;top:1120px;width:1000px;height:160px;background:var(--soft)}
.services-head h2{position:absolute;left:0;right:0;top:46px;text-align:center;font-size:24px;font-weight:600;color:var(--navy)}
.services-band{left:0;top:1272px;width:1200px;height:288px;background:var(--navy)}
.service{position:absolute;top:1320px;width:260px;text-align:center;color:var(--white)}
.service h3{font-size:14px;font-weight:600;margin:14px 0 8px}
.service p{font-size:10px;line-height:1.55;color:#c9d3de;padding:0 24px;margin-bottom:14px}
.service .more{display:inline-block;border:1px solid #5e7590;font-size:9px;padding:5px 14px;color:var(--white)}
.service-featured{left:300px;top:1240px;width:300px;height:320px;background:linear-gradient(180deg,#566a7e,#334c66)}
.service .more.green{background:var(--green);border-color:var(--green)}

/* ecommerce */
.ecom{left:200px;top:1690px;width:440px}
.ecom h2{font-size:44px;line-height:1.15;font-weight:600;color:var(--navy);margin-bottom:20px}
.ecom p{font-size:17px;line-height:1.5;color:var(--ink);margin-bottom:30px}

/* products */
.products-title{left:0;top:2080px;width:1200px;text-align:center;font-size:22px;font-weight:600;color:var(--navy)}
.card{position:absolute;top:2140px;width:262px;height:300px;background:var(--white);border:1px solid var(--line);box-shadow:0 4px 14px rgba(0,0,0,.05)}
.card-img{height:130px;margin:10px;background:linear-gradient(135deg,#c98c5a,#a56a3c 55%,#e1c6a6)}
.card h4{font-size:14px;font-weight:600;padding:6px 22px 6px}
.card p{font-size:9px;line-height:1.5;color:var(--muted);padding:0 22px}
.stars{padding:6px 22px;font-size:12px;color:#f3b51b}
.stars small{color:var(--muted);font-size:9px;margin-left:6px}
.price{position:absolute;left:20px;bottom:16px;background:var(--navy);color:var(--white);font-size:12px;font-weight:600;padding:5px 12px}
.old{position:absolute;right:20px;bottom:20px;font-size:11px;color:var(--green)}
.view-all{left:560px;top:2480px}

/* footer */
.footer{left:0;top:2580px;width:1200px;height:340px;background:var(--navy-dark);color:var(--white)}
.footer .brand{position:absolute;left:200px;top:60px;color:var(--white)}
.socials{position:absolute;left:262px;top:150px;display:flex;gap:10px}
.socials span{width:28px;height:28px;border-radius:50%;background:var(--green)}
.fcol{position:absolute;top:40px;font-size:12px;line-height:2}
.fcol h5{font-size:15px;font-weight:600;margin-bottom:6px}
.fcol .row{display:flex;gap:10px;align-items:center;color:#d3dbe4}
.qlinks{display:grid;grid-template-columns:120px 140px;color:#d3dbe4;font-size:11px;line-height:2;white-space:nowrap}
.copyright{position:absolute;left:200px;top:300px;font-size:10px;color:#b8c4d1}
</style>
</head>
<body>

<section class="abs hero"></section>
<div class="abs hero-photo" role="img" aria-label="Photo of a team collaborating around laptops in a bright office"></div>

<header class="abs site-header">
  <div class="brand"><span class="brand-dot"></span>PELIX BRIDGE</div>
  <nav class="nav"><span class="active">Home</span><span>Services</span><span>Digital Marketplace</span><span>About Us</span><span>Blog</span><span>Contact Us</span></nav>
  <div class="header-phone">+254 700 318 442</div>
  <span class="btn">Contact Now</span>
</header>

<h1 class="abs hero-title">Digital,<br>technology &amp;<br>data</h1>
<p class="abs hero-sub">Empowering innovations &amp; digital transformation across africa.</p>
<div class="abs hero-cta"><span><svg width="14" height="14" viewBox="0 0 14 14"><path d="M3 7h8M8 4l3 3-3 3" stroke="#fff" stroke-width="1.6" fill="none"/></svg></span>Discover more</div>

<div class="abs about-frame"></div>
<div class="abs about-photo" role="img" aria-label="Photo of a family working together on a laptop at home"></div>
<div class="abs about-text">
  <div class="eyebrow">Welcome to Pelix Bridge</div>
  <h2>Pelix Bridge Africa is a consultancy firm and digital marketplace dedicated to supporting africa's digital transformation.</h2>
  <p>We provide data-driven insights, strategic guidance and a curated marketplace that help African businesses adopt technology and grow with confidence.</p>
  <span class="btn-outline">About Us</span>
</div>

<div class="abs services-head"><h2>What We Do</h2></div>
<div class="abs services-band"></div>
<div class="abs service-featured" role="img" aria-label="Photo of a consultant at work, tinted blue"></div>

<div class="service" style="left:40px">
  <svg width="40" height="40" viewBox="0 0 40 40"><path d="M8 34h24M14 34l6-22 6 22M20 12V6" stroke="#2eaa4a" stroke-width="2" fill="none"/></svg>
  <h3>Digital Strategy</h3>
  <p>We help organisations plan, adopt and scale digital tools with clarity.</p>
  <span class="more">Learn More</span>
</div>
<div class="service" style="left:320px">
  <svg width="40" height="40" viewBox="0 0 40 40"><circle cx="20" cy="14" r="7" stroke="#2eaa4a" stroke-width="2" fill="none"/><path d="M7 34c2-8 8-11 13-11s11 3 13 11" stroke="#2eaa4a" stroke-width="2" fill="none"/></svg>
  <h3>Technical Expertise</h3>
  <p>Our engineers build reliable systems that fit real business needs today.</p>
  <span class="more green">Learn More</span>
</div>
<div class="service" style="left:610px">
  <svg width="40" height="40" viewBox="0 0 40 40"><rect x="9" y="5" width="22" height="30" stroke="#2eaa4a" stroke-width="2" fill="none"/><path d="M14 28v-6M20 28v-10M26 28v-4" stroke="#2eaa4a" stroke-width="2"/></svg>
  <h3>Data Analytics</h3>
  <p>We turn raw figures into insight that guides smarter decisions daily.</p>
  <span class="more">Learn More</span>
</div>
<div class="service" style="left:900px">
  <svg width="40" height="40" viewBox="0 0 40 40"><rect x="12" y="12" width="16" height="16" stroke="#2eaa4a" stroke-width="2" fill="none"/><path d="M16 12V6M24 12V6M16 34v-6M24 34v-6M6 16h6M6 24h6M28 16h6M28 24h6" stroke="#2eaa4a" stroke-width="2"/></svg>
  <h3>Artificial Intelligence &amp;<br>Machine Learning</h3>
  <p>We apply smart models that automate work and reveal new value fast.</p>
  <span class="more">Learn More</span>
</div>

<div class="abs ecom">
  <h2>e-Commerce<br>for Digital Products</h2>
  <p>Lorem Ipsum is simply dummy text of the printing and typesetting industry. Lorem Ipsum has been the industry's standard dummy text ever since.</p>
  <span class="btn">Explore Marketplace</span>
</div>

<h2 class="abs products-title">Featured Products</h2>
<div class="card" style="left:200px">
  <div class="card-img" role="img" aria-label="Photo of a laptop on a wooden desk"></div>
  <h4>Cordinary Popular Belief</h4>
  <p>Practical templates and toolkits built for growing African teams.</p>
  <div class="stars">★★★★★<small>(4 reviews)</small></div>
  <span class="price">$27</span><span class="old">$42.00</span>
</div>
<div class="card" style="left:470px">
  <div class="card-img" role="img" aria-label="Photo of a laptop on a wooden desk"></div>
  <h4>Cordinary Popular Belief</h4>
  <p>Practical templates and toolkits built for growing African teams.</p>
  <div class="stars">★★★★★<small>(4 reviews)</small></div>
  <span class="price">$27</span><span class="old">$42.00</span>
</div>
<div class="card" style="left:740px">
  <div class="card-img" role="img" aria-label="Photo of a laptop on a wooden desk"></div>
  <h4>Cordinary Popular Belief</h4>
  <p>Practical templates and toolkits built for growing African teams.</p>
  <div class="stars">★★★★★<small>(4 reviews)</small></div>
  <span class="price">$27</span><span class="old">$42.00</span>
</div>
<span class="abs btn-outline view-all">View All</span>

<footer class="abs footer">
  <div class="brand"><span class="brand-dot"></span>PELIX BRIDGE</div>
  <div class="socials"><span></span><span></span><span></span><span></span></div>
  <div class="fcol" style="left:520px">
    <h5>Contact Us</h5>
    <div class="row"><svg width="14" height="14" viewBox="0 0 14 14"><path d="M3 1l3 3-2 2c1 2 2 3 4 4l2-2 3 3-2 2C6 13 1 8 1 3z" fill="#2eaa4a"/></svg>+254 700 318 442</div>
    <div class="row"><svg width="14" height="14" viewBox="0 0 14 14"><rect x="1" y="3" width="12" height="8" stroke="#2eaa4a" fill="none"/><path d="M1 3l6 5 6-5" stroke="#2eaa4a" fill="none"/></svg>hello@pelixbridge.co.ke</div>
    <div class="row" style="align-items:flex-start"><svg width="14" height="14" viewBox="0 0 14 14" style="margin-top:6px"><path d="M7 13S2 8 2 5a5 5 0 0110 0c0 3-5 8-5 8z" fill="#2eaa4a"/></svg><span>48 Kilima Road, Westlands,<br>Nairobi 00800</span></div>
  </div>
  <div class="fcol" style="left:760px">
    <h5>Quick Links</h5>
    <div class="qlinks">
      <span>Home</span><span>Contact us</span>
      <span>Services</span><span>Terms and conditions</span>
      <span>Digital marketplace</span><span>Privacy policy</span>
      <span>About us</span><span></span>
      <span>Blog</span><span></span>
    </div>
  </div>
  <div class="copyright">© 2024 Pelix Bridge. All Rights Reserved.</div>
</footer>

</body>
</html>
```